Scientific Poster- Immunology Marcus T

I have all the information, but need this placed in a design format where it can be printed. The size will need to be 1meter by 1 meter. I just have the basic text and images. I just need the design around that added to make it look more attractive.
Please see some of the examples online, with web link below.

Target Market(s)

Scientific Meeting

Font styles to use
Sans Serif

Requirements
Must have
• Professional appearance
Nice to have
• examples can be found on
• https://www.orvelmintprints.com/sample_gallery_pages
Should not have
• Should be professional

```html
<!DOCTYPE html>
<html lang="en">
<head>
<meta charset="utf-8">
<title>Image Guided Cryoablation of Cancer with Intra-Tumor Injection of Anti-CTLA-4 and PD-1 Immune Checkpoint Inhibitors</title>
<link rel="stylesheet" href="https://fonts.googleapis.com/css2?family=Oswald:wght@600;700&family=Arimo:wght@400;700&family=Anton&display=swap">
<style>
:root{
  --teal-dark:#0d3e46;
  --teal:#1d6a70;
  --sand:#e9d98a;
  --sand-light:#f3e8ad;
  --title-cream:#f6eeb0;
  --author-yellow:#f2d63a;
  --red:#b3191c;
  --red-dark:#8a1013;
  --orange:#d9652a;
  --ice:#d9eef0;
  --ink:#1c1c1c;
  --caption:#c4161c;
  --scan:#0c1420;
}
*{box-sizing:border-box;margin:0;padding:0}
html,body{width:1200px;height:1200px;overflow:hidden}
body{font-family:"Arimo",Arial,sans-serif;color:var(--ink);position:relative;
  background:
   radial-gradient(ellipse at 20% 70%, rgba(70,120,80,.55), transparent 60%),
   radial-gradient(ellipse at 85% 55%, rgba(255,250,200,.6), transparent 55%),
   linear-gradient(135deg,#c9c46e 0%,var(--sand) 40%,var(--sand-light) 70%,#e3cd77 100%)}

.poster-header{position:absolute;left:0;top:0;width:1200px;height:160px;text-align:center;
  background:linear-gradient(180deg,var(--teal-dark),var(--teal) 65%,rgba(29,106,112,0) 100%)}
.poster-title{font-family:"Oswald",sans-serif;font-weight:700;font-size:38px;line-height:44px;
  color:var(--title-cream);letter-spacing:.5px;padding-top:12px;text-shadow:2px 2px 2px rgba(0,0,0,.55)}
.poster-authors{font-weight:700;font-size:22px;color:var(--author-yellow);margin-top:10px;
  text-shadow:1px 1px 2px rgba(0,0,0,.5)}
.poster-authors .sep{margin:0 14px;color:var(--title-cream)}

.abstract-heading{position:absolute;left:44px;top:172px;width:336px;height:44px;
  font-family:"Anton",sans-serif;font-size:34px;line-height:44px;letter-spacing:5px;color:var(--red);
  text-align:center;text-shadow:2px 2px 0 var(--title-cream),3px 3px 3px rgba(0,0,0,.3)}
.section{position:absolute;left:44px;width:336px;border:3px solid var(--red);background:var(--ice);
  box-shadow:2px 3px 5px rgba(0,0,0,.25);display:flex;flex-direction:column;overflow:hidden}
.section-title{background:linear-gradient(180deg,#c8262a,var(--red-dark));color:#fff;font-weight:700;
  font-size:18px;line-height:24px;text-align:center;padding:2px 0}
.section-body{flex:1;font-size:11.8px;line-height:14.2px;padding:7px 10px;text-align:justify}
.section-body p+p{margin-top:10px}
.hypothesis{top:222px;height:160px}
.methods{top:388px;height:316px}
.results{top:710px;height:234px}
.conclusion{top:956px;height:228px}

.patient{position:absolute;left:432px;width:768px;overflow:hidden;
  background:linear-gradient(90deg,rgba(250,245,205,.55),rgba(240,225,150,.35))}
.patient-bar{height:30px;background:linear-gradient(90deg,var(--red-dark),var(--red) 20%,var(--orange) 55%,rgba(217,101,42,0) 100%)}
.patient-label{font-family:"Anton",sans-serif;font-size:21px;line-height:30px;letter-spacing:1px;color:var(--author-yellow);
  padding-left:30px;text-shadow:1px 1px 0 #5a0a0a}
.patient-body{display:flex;gap:10px;padding:8px 10px 8px 6px}
.case-text{width:166px;flex:none;background:var(--ice);font-size:11px;line-height:13px;padding:6px 8px;text-align:justify;
  box-shadow:1px 2px 4px rgba(0,0,0,.2);align-self:flex-start}
.figures{flex:1;display:grid;grid-template-columns:repeat(3,1fr);column-gap:14px;row-gap:8px}
.figure{overflow:hidden}
.figure .scan{width:100%;background:radial-gradient(ellipse at 50% 55%,#3a4a6a 0%,#1b2438 45%,var(--scan) 80%)}
.figure .scan.pet{background:radial-gradient(ellipse at 50% 55%,#5b6fd0 0%,#23307a 45%,#070b22 80%)}
.figure .scan.ct{background:radial-gradient(ellipse at 50% 55%,#cfcfcf 0%,#6d6d6d 40%,#0b0b0b 80%)}
.figure figcaption{font-size:7px;line-height:8.4px;color:var(--caption);font-weight:700;text-align:center;margin-top:3px}

.p1{top:174px;height:290px}
.p1 .figures{grid-template-rows:repeat(2,113px)}
.p1 .scan{height:80px}
.p2{top:476px;height:366px}
.p2 .figures{grid-template-rows:repeat(3,100px)}
.p2 .scan{height:76px}
.p3{top:856px;height:338px}
.p3 .figures{grid-template-rows:repeat(2,140px)}
.p3 .scan{height:104px}
.p3 .case-text{width:170px;height:306px;font-size:8.2px;line-height:9.4px;padding:6px}
</style>
</head>
<body>
<header class="poster-header">
  <h1 class="poster-title">IMAGE GUIDED CRYOABLATION OF CANCER WITH INTRA-TUMOR INJECTION<br>OF ANTI-CTLA-4 AND PD-1 IMMUNE CHECKPOINT INHIBITORS</h1>
  <p class="poster-authors">Marcus R. Thorne MD<span class="sep">|</span>Daniel E. Whitford MD<span class="sep">|</span>Owen A. Kessler MD</p>
</header>

<h2 class="abstract-heading">ABSTRACT:</h2>
<section class="section hypothesis">
  <h3 class="section-title">Hypothesis:</h3>
  <div class="section-body"><p>In situ Image Guided Cancer Cryoablation combined with image guided injection of immune check-point inhibitors is an effective method of treating local and systemic malignancy. The inflammatory cytokines and release of tumor antigens from Cryoablation, combined with immune check-point inhibitors can create an in-situ tumor vaccine resulting in a systemic anti-cancer immune response.</p></div>
</section>
<section class="section methods">
  <h3 class="section-title">Methods:</h3>
  <div class="section-body"><p>Patients participating in an ongoing research protocol underwent in situ Image Guided Cryoablation of one or more malignant cancers. Image guidance included Computed Tomography and/or Ultrasound. The Cryoablation procedure was performed using standard well developed and described percutaneous techniques. For the procedure, each patient received either IV or general anesthesia. Immediately following the cryoablation of cancer, each cryo-treated tumor was injected with a combination of Ipilimumab/Nivolumab or Ipilimumab/Pembrolizumab immune checkpoint inhibitors. The injection was performed with 50% of the systemic dose of 3mg/kg. The patients remained monitored inpatients for 24-48 hours post surgery. Follow-up with serum tumor markers where applicable, CBC, and serum chemistries were obtained at 1 week and every month post procedure. Cross sectional Imaging was obtained at 3-4 weeks and at every 3 months post procedure.</p></div>
</section>
<section class="section results">
  <h3 class="section-title">Results:</h3>
  <div class="section-body"><p>Patients treated with in situ tumor cryoablation demonstrated the expected macro cellular cryo-necrosis with morphologic changes in the treated tissue, which was evident as early as 6 hours postop. With more time, the treated tumor morphology was noted to deviate from the standard cryoablation decay with some patients having rapid large volume tissue decay far exceeding that expected from cryoablation alone.</p><p>In the non treated tumor as identified on cross sectional imaging, distant tumor deposits were noted to decrease in size and many to disappear. At 6 months post treatment there has been no recurrence of responding tumor.</p></div>
</section>
<section class="section conclusion">
  <h3 class="section-title">Conclusion:</h3>
  <div class="section-body"><p>The combination of intra-tumoral checkpoint inhibitor injection with percutaneous cryoablation of metastatic malignancy shows great promise in providing a far superior treatment methodology than either method alone, has previously shown. It has been known that ablation techniques, especially Cryoablation can generate an anti-tumor immune response; however, this is rarely curative. These cases show that the combination of immune checkpoint inhibitors with Cryoablation generates a synergy, effectively creating a tumor vaccine, which can cause the resolution of not only the local treated area, but also a systemic</p></div>
</section>

<section class="patient p1">
  <div class="patient-bar"><h2 class="patient-label">PATIENT #1</h2></div>
  <div class="patient-body">
    <p class="case-text">Patient is a 58-year-old female with a seven-year history of tumor of unknown origin, presumed breast. She had prior standard of care treatment with chemotherapy and radiation. The patient had failed all standard options and continued to have progression with numerous tumors in the lungs and thoracic lymph nodes. The patient was then treated with image-guided ablation combined with Ipilimumab and Pembrolizumab.</p>
    <div class="figures">
      <figure class="figure"><div class="scan pet" role="img" aria-label="FDG PET/CT axial chest scan"></div><figcaption>Image above demonstrates FDG PET/CT with abnormal uptake in two right upper lobe nodules.</figcaption></figure>
      <figure class="figure"><div class="scan pet" role="img" aria-label="FDG PET/CT axial chest scan"></div><figcaption>Image above demonstrates FDG PET/CT with abnormal uptake in bilateral intra- hilar and right peri-aortic lymph nodes.</figcaption></figure>
      <figure class="figure"><div class="scan pet" role="img" aria-label="FDG PET/CT axial chest scan"></div><figcaption>Image above demonstrates FDG PET/CT with abnormal uptake in right supra-hilar lymph nodes, right upper lobe nodule and right axillary lymph node.</figcaption></figure>
      <figure class="figure"><div class="scan" role="img" aria-label="CT scan during ablation with needle in right upper lobe lesion"></div><figcaption>Image above is a CT scan performed during the ablation procedure demonstrating ablation needle with a right upper lobe lesion.</figcaption></figure>
      <figure class="figure"><div class="scan pet" role="img" aria-label="FDG PET/CT two months after treatment"></div><figcaption>The image above demonstrates a FDG PET/CT scan performed 2 months after treatment with minimal peripheral FDG uptake ofthe ablated tumor site.</figcaption></figure>
      <figure class="figure"><div class="scan pet" role="img" aria-label="FDG PET/CT two months after treatment"></div><figcaption>The above image is a FDG PET/CT performed 2 months after treatment showing resolution of intra-hilar adenopathy, with minimal residual uptake in peri-aortic adenopathy.</figcaption></figure>
    </div>
  </div>
</section>

<section class="patient p2">
  <div class="patient-bar"><h2 class="patient-label">PATIENT #2</h2></div>
  <div class="patient-body">
    <p class="case-text">Patient is a 68 year old male with a 2 year history of a left renal mass. The patient underwent a left nephrectomy with a diagnosis of renal cell carcinoma. A subsequent CT scan demonstrated numerous lung nodules (&gt;20) and a large L5 vertebral body mass. The patient was then treated with Cryoablation of the L5 mass with intra-tumoral injection of Ipilimumab and Nivolumab into the ablated tumor site. A follow up CT scan 7 weeks after treatment demonstrated complete resolution of the lung nodules with a stable L5 mass.</p>
    <div class="figures">
      <figure class="figure"><div class="scan ct" role="img" aria-label="CT chest with a lung nodule"></div><figcaption>The image above demonstrates a CT scan of the chest with a lung nodule.</figcaption></figure>
      <figure class="figure"><div class="scan ct" role="img" aria-label="CT chest with bilateral lung nodules"></div><figcaption>CT scan of the chest demonstrates multiple bilateral lung nodules.</figcaption></figure>
      <figure class="figure"><div class="scan ct" role="img" aria-label="CT chest with additional lung nodule"></div><figcaption>CT scan of the chest demonstrating additional lung nodule.</figcaption></figure>
      <figure class="figure"><div class="scan" role="img" aria-label="CT lumbar spine with L5 mass"></div><figcaption>CT scan of the lumbar spine demonstrating L5 mass.</figcaption></figure>
      <figure class="figure"><div class="scan" role="img" aria-label="CT during cryoablation of L5 mass"></div><figcaption>CT scan during ablation procedure demonstrating Cryoablation of L5 mass.</figcaption></figure>
      <figure class="figure"><div class="scan ct" role="img" aria-label="CT chest seven weeks after procedure"></div><figcaption>CT scan 7 weeks after procedure demonstrating resolution of lung nodules.</figcaption></figure>
      <figure class="figure"><div class="scan ct" role="img" aria-label="CT chest seven weeks after procedure"></div><figcaption>CT scan 7 weeks after procedure demonstrating resolution of lung nodule.</figcaption></figure>
      <figure class="figure"><div class="scan ct" role="img" aria-label="CT chest seven weeks after procedure"></div><figcaption>CT scan 7 weeks after procedure demonstrating resolution of lung nodules.</figcaption></figure>
      <figure class="figure"><div class="scan" role="img" aria-label="CT lumbar spine seven weeks after treatment"></div><figcaption>CT scan of the lumbar spine 7 weeks after treatment demonstrating stable lumbar mass.</figcaption></figure>
    </div>
  </div>
</section>

<section class="patient p3">
  <div class="patient-bar"><h2 class="patient-label">PATIENT #3</h2></div>
  <div class="patient-body">
    <p class="case-text">Patient is a 54 year old female with a several year history of breast cancer who then developed non-small cell lung cancer. The patient underwent several years of treatment with standard chemotherapy and radiation. The patient then developed a new large lung mass with mediastina adenopathy. A new biopsy was performed demonstrating malignancy of neuroendocrine type. The patient, opted for no further chemotherapy, but did agree to Cryoablation combined with intra-tumoral injection of Ipilimumab and Nivolumab. Due to the large volume of tumor, only a small area of tumor was ablated and treated. However, by 2 months, the patient demonstrated a whole body systemic response with resolution of tumors beyond the ablation site. This further supports that ablation combined with immune checkpoint inhibitors can create a systemic, anti-tumor immune response, essentially an in-situ tumor vaccine.</p>
    <div class="figures">
      <figure class="figure"><div class="scan pet" role="img" aria-label="PET/CT with right hilar and subcarinal uptake"></div><figcaption>Image demonstrates PET/CT with abnormal right hilar and subcarinal lymph nodes.</figcaption></figure>
      <figure class="figure"><div class="scan" role="img" aria-label="CT with mediastinal and right hilar mass"></div><figcaption>Image demonstrates a large mediastinal and right hilar mass prior to the Cryoablation procedure combined with immune checkpoint injection.</figcaption></figure>
      <figure class="figure"><div class="scan" role="img" aria-label="CT during cryoablation with needle in subcarinal node"></div><figcaption>Image demonstrates Cryoablation procedure with the needle placed within the subcarinal lymph node.</figcaption></figure>
      <figure class="figure"><div class="scan" role="img" aria-label="CT after treatment of subcarinal node"></div><figcaption>Image demonstrates normal expected low attenuation with the treated subcarinal lymph node, which is a typical post Cryoablation appearance.</figcaption></figure>
      <figure class="figure"><div class="scan" role="img" aria-label="One month follow up CT"></div><figcaption>One month follow up CT demonstrates significant reduction in the associated mediastinal and right hilar mass.</figcaption></figure>
      <figure class="figure"><div class="scan pet" role="img" aria-label="Two month follow up PET/CT"></div><figcaption>Two month follow up PET/CT shows resolution of mediastinal and right hilar masses.</figcaption></figure>
    </div>
  </div>
</section>
</body>
</html>
```